Gentle Brook toothpaste tube design

Design a Gentle Brook tube design for our all natural toothpaste. The toothpaste is 100% natural with a smooth marshmallow consistency. It's unique because it's not pastelike at all. The all natural flavors make the toothpaste taste great. The toothpaste is smooth yet still leaves your mouth feeling squeaky clean. We want to market this as an all natural family toothpaste.

The flavor is Mint. (possibly called "Cozy Mint")

We have included our logo (eps & jpg), information that goes on the back of the tube, and the artwork template from the tube supplier for the 4.2oz tube.

We like a vintage earthy retro look and feel but we are not limited to this.

The tubes stand upright as shown in the picture of File 4.
Updates

The finished artwork must include anĀ adobe illustratorĀ file.

Project Deadline Extended

I would like to thank all of the designers for their work on this project. We had a difficult time making a decision since all of the designs were very close to what we expected.

Sincerely,

Wes

Target Market(s)

The target market is families that desire an all natural toothpaste. We will be stressing the 100% natural and great taste.

Requirements
Must have
• Three colors maximum due to tube manufacture restrictions.

Must have "100% natural" and "fluoride free" on front of tube. A reference to the great taste or flavor is also important.

Must say 4.2 oz on the front of the tube, centered, at the bottom.
Nice to have
• Fun, colorful packaging that will stand out. Go to your local store and stand in front of the tootpaste shelves, give us something different!
Should not have
• We do not want a lot of red or blue because these are predominate colors already in use on toothpaste tubes and boxes.

```html
<!DOCTYPE html>
<html lang="en">
<head>
<meta charset="utf-8">
<title>Gentle Brook Toothpaste – Tube Artwork</title>
<link href="https://fonts.googleapis.com/css2?family=Archivo:wght@600;800&family=Italianno&display=swap" rel="stylesheet">
<style>
  :root {
    --stage: #e6e6e4;
    --tube-light: #f5f5f3;
    --tube-mid: #e4eadb;
    --tube-green: #b7cc98;
    --green-dark: #3f6a26;
    --green-mid: #5f8f33;
    --green-light: #7fa83e;
    --herb: #6f934a;
    --crimp: #ecece8;
    --crimp-line: #c9cbc2;
  }
  * { margin: 0; padding: 0; box-sizing: border-box; }
  html, body {
    width: 1200px; height: 900px; overflow: hidden;
    background: var(--stage);
  }
  .canvas {
    position: relative; width: 1200px; height: 900px;
    display: flex; align-items: center; justify-content: center;
  }
  .tube-artwork {
    position: relative; width: 1100px; height: 440px;
    background: linear-gradient(90deg, var(--tube-light) 0%, var(--tube-light) 35%, var(--tube-mid) 62%, var(--tube-green) 100%);
    overflow: hidden;
  }
  .crimp-seal {
    position: absolute; right: 0; top: 0; width: 34px; height: 100%;
    background: repeating-linear-gradient(180deg, var(--crimp) 0 4px, var(--crimp-line) 4px 5px);
    border-left: 1px solid var(--crimp-line);
  }
  .herb-illustration {
    position: absolute; left: 780px; top: 0; width: 286px; height: 100%;
    background: radial-gradient(ellipse at 60% 30%, rgba(111,147,74,0.45), rgba(111,147,74,0) 60%),
                radial-gradient(ellipse at 40% 85%, rgba(111,147,74,0.4), rgba(111,147,74,0) 55%);
  }
  .brand-lockup {
    position: absolute; left: 60px; top: 190px;
    display: flex; align-items: center; gap: 12px;
  }
  .brand-dot {
    width: 28px; height: 28px; border-radius: 50%;
    background: var(--green-light);
  }
  .brand-name {
    font-family: "Archivo", sans-serif; font-weight: 800;
    font-size: 40px; color: var(--green-dark); letter-spacing: -0.5px;
    white-space: nowrap;
  }
  .claim-block {
    position: absolute; left: 400px; top: 96px;
    font-family: "Archivo", sans-serif; line-height: 1;
  }
  .claim-percent { font-weight: 800; font-size: 56px; color: var(--green-light); }
  .claim-natural { font-weight: 800; font-size: 70px; color: var(--green-dark); margin-top: 6px; letter-spacing: 0.5px; }
  .claim-product { font-weight: 600; font-size: 50px; color: var(--green-mid); margin-top: 8px; letter-spacing: 0.5px; }
  .claim-free { font-weight: 800; font-size: 26px; color: var(--green-light); margin-top: 14px; letter-spacing: 0.5px; }
  .net-weight {
    position: absolute; left: 0; right: 0; bottom: 22px;
    text-align: center;
    font-family: "Archivo", sans-serif; font-weight: 600;
    font-size: 20px; color: var(--green-dark); letter-spacing: 0.5px;
  }
  .script-word {
    position: absolute; font-family: "Italianno", cursive;
    color: var(--green-dark); opacity: 0.8; white-space: nowrap;
    line-height: 1;
  }
  .script-flavor { left: 830px; top: 70px; font-size: 44px; transform: rotate(-8deg); }
  .script-family { left: 905px; top: 180px; font-size: 42px; transform: rotate(-62deg); }
  .script-natural { left: 805px; top: 300px; font-size: 38px; transform: rotate(-70deg); }
  .script-organic { left: 945px; top: 270px; font-size: 40px; transform: rotate(-14deg); }
</style>
</head>
<body>
<main class="canvas">
  <section class="tube-artwork">
    <div class="herb-illustration" role="img" aria-label="Sketched mint and herb sprigs in green ink"></div>

    <div class="brand-lockup">
      <span class="brand-dot"></span>
      <span class="brand-name">Gentle Brook</span>
    </div>

    <div class="claim-block">
      <p class="claim-percent">100%</p>
      <p class="claim-natural">NATURAL</p>
      <p class="claim-product">TOOTHPASTE</p>
      <p class="claim-free">FLUORIDE FREE</p>
    </div>

    <span class="script-word script-flavor">Cozy Mint</span>
    <span class="script-word script-family">Family</span>
    <span class="script-word script-natural">Natural</span>
    <span class="script-word script-organic">Organic</span>

    <p class="net-weight">4.2 oz</p>

    <div class="crimp-seal"></div>
  </section>
</main>
</body>
</html>
```